www.copperleaf-nimbo.com web Page

Discover Quito Discover Otavalo Discover Cotopaxi Discover Discover Discover Mindo Birdwatching Discover Quilotoa Discover Amazonas Discover Galapagos Islands
Updates

Thank you all sending proyect designs..If you have not received a reply from us than your design has not met our original requirements .... Best Regards, Ruben

Target Market(s)

USA / Europe England,

Number of Pages Required

5+ page

Font styles to use
Sans Serif

Requirements
Must have
• I will need Logo to be upgraded instead of 17 years, it need to say 25 years. Userfriendly design, SEO friendly and responsive. Web needs to work on all devices like Android, IOS, Tablet and Windows
Nice to have
• Please consider 1. Minimalistic design 2. Copperleaf Nimbo logo in feautred areas fo web pages 3. Modular design 4. Hero not sliding images 5. Landing page with full with image 6. Elements with animations 7. Hamburger menu 8. I will drop the Packages part of www.copperleaf-nimbo.com 9. Incorporate Galapagos Islands instead 10. I will concentrate on the modular design to have Discover Quito Discover Otavalo Discover Cotopaxi Discover Discover Discover Mindo Birdwatching Discover Quilotoa Discover Amazonas Discover Galapagos Islands
Should not have
• Sliding images

```html
<!DOCTYPE html>
<html lang="en">
<head>
<meta charset="utf-8">
<title>Copperleaf Nimbo – Discover Cotopaxi</title>
<link rel="stylesheet" href="https://fonts.googleapis.com/css2?family=Open+Sans:ital,wght@0,400;0,600;0,700;1,400&display=swap">
<style>
:root{
  --green:#2bc158;
  --ink:#111111;
  --muted:#9a9a9a;
  --soft-bg:#eceff1;
  --footer:#252a36;
  --footer-text:#8b909c;
  --white:#ffffff;
}
*{box-sizing:border-box;margin:0;padding:0}
html,body{width:1200px;height:2748px;overflow:hidden}
body{font-family:"Open Sans",Arial,sans-serif;color:var(--ink);background:var(--white);position:relative}
.center{text-align:center}

/* Hero */
.hero{position:absolute;left:0;top:0;width:1200px;height:549px}
.hero-bg{position:absolute;inset:0;
  background:linear-gradient(180deg,#7f97b0 0%,#b7c3cc 28%,#d9dcd9 40%,#9d8a6a 60%,#a4692f 80%,#6e4420 100%)}
.brand{position:absolute;left:86px;top:66px;display:flex;align-items:center;gap:10px;color:var(--white);font-weight:700;font-size:20px}
.brand-mark{width:18px;height:18px;background:var(--green)}
.top-contact{position:absolute;top:60px;font-size:10px;color:var(--white);display:flex;align-items:center;gap:8px}
.book-btn{position:absolute;left:920px;top:55px;width:152px;height:27px;border:1px solid var(--white);color:var(--white);font-size:10px;display:flex;align-items:center;justify-content:center}
.burger{position:absolute;left:1088px;top:55px;width:31px;height:27px;border:1px solid var(--white);border-radius:3px;display:flex;flex-direction:column;justify-content:center;align-items:center;gap:3px}
.burger span{display:block;width:15px;height:2px;background:var(--white)}
.hero-title{position:absolute;left:0;width:1200px;top:236px;font-size:48px;font-weight:600;color:var(--white)}
.hero-sub{position:absolute;left:400px;width:400px;top:314px;font-size:12px;line-height:22px;color:var(--white)}

/* Section headings */
.sec-title{position:absolute;left:0;width:1200px;font-size:36px;font-weight:600;color:var(--ink)}
.sec-sub{position:absolute;left:0;width:1200px;font-size:14px;color:var(--muted);letter-spacing:.5px}

/* Welcome */
.welcome{position:absolute;left:0;top:549px;width:1200px;height:458px;background:var(--soft-bg)}
.feature{position:absolute;top:170px;width:300px}
.feature .icon{width:84px;height:84px;border-radius:50%;background:var(--green);margin:0 auto;display:flex;align-items:center;justify-content:center}
.feature h3{font-size:22px;font-weight:400;margin-top:22px}
.feature p{font-size:12px;line-height:22px;color:var(--muted);margin-top:10px}

/* Gallery */
.tile{position:absolute;background:#ccc}
.tile-label{position:absolute;background:var(--green);color:var(--white);font-size:12px;display:flex;align-items:center;justify-content:center}

/* Subscribe */
.subscribe{position:absolute;left:0;top:1731px;width:1200px;height:215px}
.subscribe-bg{position:absolute;inset:0;
  background:linear-gradient(90deg,#2e9a5c 0%,#3aa56a 45%,#52a877 70%,#3d9c68 100%)}
.sub-title{position:absolute;left:137px;top:40px;font-size:38px;font-weight:700;color:var(--white);line-height:1.2}
.sub-text{position:absolute;left:137px;top:93px;width:500px;font-size:12px;line-height:22px;color:var(--white)}
.sub-more{position:absolute;left:137px;top:150px;font-size:12px;color:var(--white)}
.sub-btn{position:absolute;left:894px;top:81px;width:154px;height:44px;background:#000;color:var(--white);font-size:12px;display:flex;align-items:center;justify-content:center;border-radius:2px}

/* Testimonials */
.traveller{position:absolute;left:165px;top:1969px;width:330px;height:357px;background:linear-gradient(180deg,#f3ece3 0%,#e8d6c6 55%,#2f5fa8 100%)}
.quote-mark{position:absolute;left:505px;top:2018px;font-size:84px;font-weight:700;color:var(--green);line-height:1}
.t-title{position:absolute;left:579px;top:2026px;font-size:38px;font-weight:600;line-height:1.2}
.t-sub{position:absolute;left:582px;top:2081px;font-size:14px;color:var(--muted)}
.t-text{position:absolute;left:582px;top:2124px;width:440px;font-size:12px;line-height:22px;font-style:italic;color:var(--muted)}
.t-name{position:absolute;left:579px;top:2227px;font-size:11px;color:var(--green)}
.t-avatar{position:absolute;left:1007px;top:2185px;width:74px;height:74px;border-radius:50%;background:linear-gradient(135deg,#f0e2d6,#d9b99e)}

/* Footer */
.footer{position:absolute;left:0;top:2326px;width:1200px;height:422px;background:var(--footer);color:var(--footer-text);font-size:11px}
.social{position:absolute;left:121px;top:67px;display:flex;gap:5px}
.social span{width:31px;height:31px;border:1px solid #5a6070;border-radius:3px}
.f-rule{position:absolute;left:121px;top:142px;width:309px;height:1px;background:#3b4150}
.f-address{position:absolute;left:121px;top:168px;line-height:22px}
.f-input{position:absolute;left:115px;top:239px;width:251px;height:42px;border:1px solid #353b4a;font-size:10px;padding-left:16px;display:flex;align-items:center;color:#5e6473}
.f-btn{position:absolute;left:376px;top:239px;width:122px;height:42px;background:var(--green);color:var(--white);font-size:12px;display:flex;align-items:center;justify-content:center}
.f-copy{position:absolute;left:115px;top:321px;font-size:10px}
.f-col{position:absolute;top:62px}
.f-col h4{color:var(--white);font-size:13px;font-weight:600;margin-bottom:14px}
.f-col li{list-style:none;line-height:22px}
.f-brand{position:absolute;left:990px;top:300px;display:flex;align-items:center;gap:8px;color:var(--white);font-weight:700;font-size:16px}
.f-brand .brand-mark{width:14px;height:14px}
</style>
</head>
<body>

<header class="hero">
  <div class="hero-bg" role="img" aria-label="Snow-capped Cotopaxi volcano above golden grassland under a misty sky"></div>
  <div class="brand"><span class="brand-mark"></span>Copperleaf Nimbo</div>
  <div class="top-contact" style="left:494px">
    <svg width="14" height="14" viewBox="0 0 24 24" fill="none" stroke="#fff" stroke-width="2"><path d="M5 3h4l2 5-3 2a12 12 0 0 0 6 6l2-3 5 2v4a2 2 0 0 1-2 2A18 18 0 0 1 3 5a2 2 0 0 1 2-2z"/></svg>
    24 Hours Phone: (593+2) 410 7781
  </div>
  <div class="top-contact" style="left:712px">
    <svg width="14" height="14" viewBox="0 0 24 24" fill="none" stroke="#fff" stroke-width="2"><rect x="6" y="3" width="12" height="6"/><rect x="3" y="9" width="18" height="9" rx="1"/><rect x="7" y="14" width="10" height="7"/></svg>
    Phone/Fax: (593+2) 410 7790
  </div>
  <div class="book-btn">Book Our Day Tours!</div>
  <div class="burger"><span></span><span></span><span></span></div>
  <h1 class="hero-title center">Discover Cotopaxi</h1>
  <p class="hero-sub center">Los Amigos del Bosque Verdeluz (Friends of the Verdeluz Cloud Forest) was established</p>
</header>

<section class="welcome">
  <h2 class="sec-title center" style="top:61px">Welcome Our Company</h2>
  <p class="sec-sub center" style="top:113px">YOUR PERFECT VACATION</p>

  <div class="feature center" style="left:125px">
    <div class="icon"><svg width="38" height="38" viewBox="0 0 24 24" fill="none" stroke="#fff" stroke-width="1.5"><path d="M3 6l6-2 6 2 6-2v14l-6 2-6-2-6 2z"/><path d="M9 4v14M15 6v14"/></svg></div>
    <h3>Explore</h3>
    <p>Los Amigos del Bosque Verdeluz<br>(Friends of the Verdeluz Cloud Forest)<br>was established in 2004.</p>
  </div>
  <div class="feature center" style="left:449px">
    <div class="icon"><svg width="38" height="38" viewBox="0 0 24 24" fill="none" stroke="#fff" stroke-width="1.5"><path d="M3 14l18-6-2-2-7 2-5-4-2 1 3 5-4 1-2-2-1 1z"/><path d="M3 19h18"/></svg></div>
    <h3>Destinations</h3>
    <p>Los Amigos del Bosque Verdeluz<br>(Friends of the Verdeluz Cloud Forest)<br>was established in 2004.</p>
  </div>
  <div class="feature center" style="left:766px">
    <div class="icon"><svg width="38" height="38" viewBox="0 0 24 24" fill="none" stroke="#fff" stroke-width="1.5"><path d="M12 4L3 20h18z"/><path d="M12 4l-3-2M12 4l3-2M12 12l-3 8M12 12l3 8"/></svg></div>
    <h3>Camping</h3>
    <p>Los Amigos del Bosque Verdeluz<br>(Friends of the Verdeluz Cloud Forest)<br>was established in 2004.</p>
  </div>
</section>

<h2 class="sec-title center" style="top:1075px">Different Way To Travel</h2>
<p class="sec-sub center" style="top:1128px">YOUR PERFECT VACATION</p>

<div class="tile" style="left:139px;top:1211px;width:297px;height:383px;background:linear-gradient(160deg,#8fb83a,#3f7a2e 55%,#2a4a1e)" role="img" aria-label="Green hummingbird with orange throat perched on a branch"></div>
<div class="tile-label" style="left:139px;top:1594px;width:297px;height:42px">Ecuador Birds</div>

<div class="tile" style="left:452px;top:1211px;width:297px;height:165px;background:linear-gradient(180deg,#dfe4ea,#a9a39b)" role="img" aria-label="Gothic basilica towers in Quito"></div>
<div class="tile-label" style="left:452px;top:1376px;width:297px;height:44px">Quito, Ecuador</div>

<div class="tile" style="left:452px;top:1436px;width:297px;height:158px;background:linear-gradient(135deg,#3e5a2c,#7b6a4a 50%,#2e3a22)" role="img" aria-label="Spotted wild cat resting in the forest"></div>
<div class="tile-label" style="left:452px;top:1594px;width:297px;height:42px">Oncilla</div>

<div class="tile" style="left:766px;top:1211px;width:296px;height:383px;background:linear-gradient(180deg,#b9cfd8,#4f7a3a 40%,#c9d6d8 75%,#3d5a33)" role="img" aria-label="Tall waterfall in a green gorge"></div>
<div class="tile-label" style="left:766px;top:1594px;width:296px;height:42px">San Rafael Falls</div>

<section class="subscribe">
  <div class="subscribe-bg" role="img" aria-label="Traveller overlooking a green valley, tinted green"></div>
  <h2 class="sub-title">Subscribe Now</h2>
  <p class="sub-text">Los Amigos del Bosque Verdeluz (Friends of the Verdeluz Cloud Forest) was established in 2004. The main objective of the Foundation is the prom</p>
  <p class="sub-more">Read More</p>
  <div class="sub-btn">SUBSRIBE!</div>
</section>

<div class="traveller" role="img" aria-label="Surprised traveller with sun hat and blue suitcase"></div>
<div class="quote-mark">“</div>
<h2 class="t-title">Testimonials</h2>
<p class="t-sub">YOUR PERFECT VACATION</p>
<p class="t-text">Los Amigos del Bosque Verdeluz (Friends of the Verdeluz Cloud Forest) was established in 2004. The main objective of the Foundation is the prom Los Amigos del Bosque Verdeluz (Friends of the</p>
<p class="t-name">- NAME HERE</p>
<div class="t-avatar" role="img" aria-label="Reviewer portrait"></div>

<footer class="footer">
  <div class="social"><span></span><span></span><span></span></div>
  <div class="f-rule"></div>
  <p class="f-address">Address: Calle Los Alisos N4-22 y Pasaje Ortega, Quito<br>Tel/Fax: 593-2-410-7790</p>
  <div class="f-input">Enter your email *</div>
  <div class="f-btn">SUBSRIBE!</div>
  <p class="f-copy">© 2018 COPPERLEAF NIMBO</p>

  <div class="f-col" style="left:581px">
    <h4>CONTACT</h4>
    <ul><li>Copperleaf Nimbo S.A.</li><li>24 Hours Service: 593-2-410-7781</li><li>Email: info@copperleaf-nimbo.com</li></ul>
  </div>
  <div class="f-col" style="left:874px">
    <h4>ECUADOR FAQ</h4>
    <ul><li>About Ecuador</li><li>Tips for the Tourist</li><li>10 Reasons for travelling to Ecuador</li><li>Experiences</li><li>Moments</li><li>Connectivity</li></ul>
  </div>
  <div class="f-brand"><span class="brand-mark"></span>Copperleaf Nimbo</div>
</footer>

</body>
</html>
```